a business advisory consulting website

I need a website 3-5 pages to sell my professional services in IT and Project management Consulting. My company name is Northwell Strategy Consulting. I want it to be device friendly and easy to navigate for the busy executive however intriguing enough.
I have attached some info I drafted on About the company and personal Bio. Also there is a website that I really like that I have attached the initial site pdf and websites that I like are here: https://quillmarshcapital.example, https://tandermoviews.example, https://www.felkinlearningconsulting.example as examples. Thanks
Updates

Hi Designers, I have uploaded the logo in 3D .png format, to assist in the web design.

Target Market(s)

B2B, governments, IT companies, Project Management companies and Consulting firms, small medium enterprises to large corporate enterprises.

Industry/Entity Type

It Professional

Coding

Coded - Design and coding required

Number of Pages Required

5+ page

Font styles to use
Sans Serif

Requirements
Must have
• Home, About company, the team, what we do and contact us
Nice to have
• Blog
Should not have
• pop ups, flash

```html
<!DOCTYPE html>
<html lang="en">
<head>
<meta charset="utf-8">
<title>Northwell Strategy Consulting</title>
<link rel="stylesheet" href="https://fonts.googleapis.com/css2?family=Roboto:wght@300;400;500;700;900&family=Open+Sans:wght@400;600;700&display=swap">
<style>
:root{
  --navy:#232a4a;
  --red:#e3252a;
  --ink:#222;
  --text:#555;
  --muted:#999;
  --line:#ccc;
  --footer:#333;
  --white:#fff;
}
*{box-sizing:border-box;margin:0;padding:0}
html,body{width:1200px;height:4089px;overflow:hidden}
body{font-family:"Open Sans",sans-serif;color:var(--text);background:var(--white);position:relative}
.abs{position:absolute}
.heading{font-family:"Roboto",sans-serif}

/* header */
.site-header{top:0;left:0;width:1200px;height:96px;z-index:3}
.brand{left:100px;top:22px;display:flex;align-items:center;gap:10px}
.brand-mark{width:44px;height:44px;background:var(--red)}
.brand-name{font-family:"Roboto",sans-serif;font-weight:700;font-size:20px;line-height:22px;color:var(--navy);text-transform:uppercase}
.main-nav{right:116px;top:36px;display:flex;gap:35px;font-family:"Roboto",sans-serif;font-size:14px;color:#888;text-transform:uppercase}
.main-nav .active{color:var(--red)}
.header-rule{left:100px;top:95px;width:1000px;height:2px;background:#ddd}

/* hero */
.hero{top:0;left:0;width:1200px;height:605px;background:linear-gradient(180deg,#fdfdfd 0%,#e7eaee 35%,#b7bec7 70%,#8c949e 100%)}
.hero-figure{left:210px;top:180px;width:220px;height:410px;background:linear-gradient(180deg,#5c6170,#2b2f3d);border-radius:40px 40px 6px 6px;opacity:.7}
.hero-kicker{left:487px;top:202px;font-family:"Roboto",sans-serif;font-size:27px;letter-spacing:5px;color:var(--ink)}
.hero-title{left:487px;top:250px;font-family:"Roboto",sans-serif;font-weight:900;font-size:80px;line-height:66px;color:#000;text-transform:uppercase;letter-spacing:-1px}
.hero-title .light{font-weight:300}
.hero-btn{left:487px;top:471px;width:188px;height:43px;background:var(--white);font-family:"Roboto",sans-serif;font-weight:700;font-size:17px;letter-spacing:4px;color:var(--ink);display:flex;align-items:center;justify-content:center}

/* consulting */
.intro-text{left:609px;top:710px;width:490px;font-size:14px;line-height:25px}
.link-more{font-family:"Roboto",sans-serif;font-size:14px;letter-spacing:2px;color:var(--navy);text-transform:uppercase;padding-bottom:6px;border-bottom:4px solid var(--navy)}
.intro-more{left:609px;top:828px}
.point{width:230px}
.point-num{font-family:"Roboto",sans-serif;font-weight:700;font-size:40px;color:var(--red);line-height:1}
.point-title{margin-top:24px;font-family:"Roboto",sans-serif;font-weight:700;font-size:17px;letter-spacing:2px;line-height:21px;color:var(--ink);text-transform:uppercase}
.point-body{margin-top:20px;font-size:13.5px;line-height:22px}
.consult-title{left:127px;top:1052px;font-family:"Roboto",sans-serif;font-weight:900;font-size:66px;color:var(--navy);text-transform:uppercase}

/* services band */
.band-photo{top:1222px;left:0;width:813px;height:706px;background:linear-gradient(135deg,#3a3a3a 0%,#8a8a8a 45%,#d8d8d8 70%,#6a6a6a 100%)}
.band-side{top:1222px;left:1098px;width:102px;height:706px;background:linear-gradient(180deg,#bbb,#eaeaea 50%,#c8c8c8)}
.service{left:813px;width:285px;padding:0 28px}
.service .icon{width:40px;height:40px}
.service-title{margin-top:28px;font-family:"Roboto",sans-serif;font-weight:700;font-size:17px;letter-spacing:2px;line-height:21px;color:var(--ink);text-transform:uppercase}
.service-body{margin-top:16px;font-size:12px;line-height:19px}
.service-why{top:1222px;height:259px;background:var(--white);padding-top:56px}
.service-process{top:1481px;height:219px;background:var(--red);padding-top:24px}
.service-process .service-title,.service-process .service-body{color:var(--white)}
.service-tech{top:1700px;height:228px;background:var(--white);padding-top:30px}

/* testimonial */
.quote{left:280px;top:2006px;width:640px;text-align:center;font-size:14px;line-height:28px}
.avatar{left:489px;top:2116px;width:222px;height:222px;border-radius:50%;background:radial-gradient(circle at 50% 40%,#dcdcdc,#8a8a8a)}
.role{left:0;top:2356px;width:1200px;text-align:center;font-family:"Roboto",sans-serif;font-size:17px;letter-spacing:8px;color:var(--red)}
.person{left:0;top:2384px;width:1200px;text-align:center;font-family:"Roboto",sans-serif;font-weight:900;font-size:64px;color:var(--navy);text-transform:uppercase}
.btn-outline{left:530px;top:2487px;width:139px;height:42px;border:2px solid var(--navy);font-family:"Roboto",sans-serif;font-weight:500;font-size:14px;color:var(--navy);display:flex;align-items:center;justify-content:center}
.arrow{top:2244px;width:26px;height:46px}
.dots{left:570px;top:2595px;display:flex;gap:6px}
.dots span{width:26px;height:3px;background:#ccc}
.dots span.on{background:#999}

/* blog */
.blog{top:2608px;left:0;width:1200px;height:630px;background:var(--navy)}
.blog-title{left:0;top:2655px;width:1200px;text-align:center;font-family:"Roboto",sans-serif;font-weight:900;font-size:62px;color:var(--white)}
.post-img{top:2772px;width:465px;height:261px;background:linear-gradient(135deg,#e8e8e8,#9a9a9a 60%,#cfcfcf)}
.post-card{top:2973px;width:243px;height:168px;background:var(--white);padding:30px 18px}
.post-title{font-family:"Roboto",sans-serif;font-weight:700;font-size:17px;color:var(--ink);text-transform:uppercase}
.post-body{margin-top:10px;font-size:13px;line-height:22px}
.post-link{display:inline-block;margin-top:14px;font-size:13px;color:var(--red);text-transform:uppercase;border-bottom:1px solid var(--red);padding-bottom:2px}

/* contact */
.contact-title{left:127px;top:3318px;font-family:"Roboto",sans-serif;font-weight:900;font-size:64px;line-height:70px;color:var(--navy);text-transform:uppercase}
.field-label{left:135px;font-size:13px;color:var(--ink)}
.field{left:135px;width:513px;border:1px solid #bbb;background:var(--white);font-size:13px;color:#aaa;padding:9px 10px}
.submit{left:135px;top:3792px;width:107px;height:42px;border:2px solid #bbb;font-size:13px;color:#aaa;display:flex;align-items:center;justify-content:center;text-transform:uppercase}
.social-head{left:709px;top:3354px;font-family:"Roboto",sans-serif;font-size:17px;letter-spacing:4px;color:var(--red);text-transform:uppercase}
.social{left:709px}
.social-box{width:50px;height:50px;background:#8a8e99;border-radius:4px;margin-left:3px}
.social-name{margin-top:18px;font-weight:700;font-size:14px;color:var(--ink)}
.social-handle{font-size:14px;color:var(--ink)}

/* footer */
.site-footer{top:3923px;left:0;width:1200px;height:166px;background:var(--footer)}
.footer-nav{left:0;top:3962px;width:1200px;display:flex;justify-content:center;gap:36px;font-family:"Roboto",sans-serif;font-size:14px;color:#bbb;text-transform:uppercase}
.footer-nav .active{color:var(--red)}
.copyright{left:0;top:4014px;width:1200px;text-align:center;font-size:13px;color:#aaa}
.copyright b{color:#ccc}
</style>
</head>
<body>

<section class="abs hero" role="img" aria-label="Businessman in a suit looking out over a city skyline from a balcony"></section>
<div class="abs hero-figure" role="img" aria-label="Standing businessman seen from behind"></div>

<header class="abs site-header">
  <div class="abs brand"><span class="brand-mark"></span><span class="brand-name">Northwell<br>Strategy</span></div>
  <nav class="abs main-nav"><span class="active">Home</span><span>About Company</span><span>The Team</span><span>What We Do</span><span>Blog</span><span>Contact Us</span></nav>
  <div class="abs header-rule"></div>
</header>

<div class="abs hero-kicker">PROFESSIONAL SERVICES IN</div>
<h1 class="abs hero-title">IT <span class="light">AND</span><br>PROJECT<br>MANAGEMENT</h1>
<div class="abs hero-btn">READ MORE</div>

<p class="abs intro-text">We're known for our pragmatism, in depth analysis, strategic insight and nurturing long-term client self-sufficiency. We approach business consulting differently, with a Genuine Client Partnership model that builds client capability and rightsized solutions for the client.</p>
<span class="abs link-more intro-more">Read More</span>

<div class="abs point" style="left:609px;top:898px">
  <div class="point-num">01</div>
  <div class="point-title">Efficiency and<br>Effectiveness</div>
  <p class="point-body">We strive for efficiency and effectiveness when assisting our clients optimize their operational structures to maximize revenue and returns</p>
</div>
<div class="abs point" style="left:859px;top:898px">
  <div class="point-num">02</div>
  <div class="point-title">Grow and<br>Scale</div>
  <p class="point-body">We exist to help grow and scale business operations, rationalize costs for early-stage startups, Small and Medium Sized Enterprises (SMEs)</p>
</div>
<h2 class="abs consult-title">Consulting</h2>

<div class="abs band-photo" role="img" aria-label="Black and white close-up of a hand touching a tablet screen"></div>
<div class="abs band-side" role="img" aria-label="Soft grey continuation of the tablet photograph"></div>

<div class="abs service service-why">
  <svg class="icon" viewBox="0 0 40 40" fill="none" stroke="#222" stroke-width="1.5"><circle cx="20" cy="16" r="9"/><path d="M16 25v5h8v-5M17 33h6M20 2v3M6 16H3M37 16h-3M9 6l2 2M31 6l-2 2"/></svg>
  <div class="service-title">Why<br>We Exist</div>
  <p class="service-body">We help you scale your business operations to become highly profitable.</p>
</div>
<div class="abs service service-process">
  <svg class="icon" viewBox="0 0 40 40" fill="none" stroke="#fff" stroke-width="1.5"><circle cx="18" cy="22" r="14"/><circle cx="18" cy="22" r="9"/><circle cx="18" cy="22" r="4"/><path d="M18 22L34 6M30 4v6h6"/></svg>
  <div class="service-title">Process<br>Improvement</div>
  <p class="service-body">We work closely with public sector bodies to drive cost and efficiency gains</p>
</div>
<div class="abs service service-tech">
  <svg class="icon" viewBox="0 0 40 40" fill="none" stroke="#222" stroke-width="1.5"><path d="M3 14l8-8 8 6 6-4 12 10-4 4M3 14l14 16 4-3 4 3 3-3 4 2 3-4M14 20l5 5M18 17l6 6M22 14l6 6"/></svg>
  <div class="service-title">Technology<br>Analysis</div>
  <p class="service-body">We work closely with both the Public sector health services</p>
</div>

<p class="abs quote">Aenean pulvinar dui ornare, feugiat lorem non, ultrices justo. Mauris efficitur, mauris in auctor euismod, quam elit ultrices urna, eget eleifend arcu risus id metus. Maecenas ex enim, mattis eu velit vitae, blandit mattis sapien. Sed aliquam leo et semper vestibulum.</p>
<svg class="abs arrow" style="left:10px" viewBox="0 0 26 46" fill="none" stroke="#222" stroke-width="2"><path d="M24 2L3 23l21 21"/></svg>
<svg class="abs arrow" style="left:1164px" viewBox="0 0 26 46" fill="none" stroke="#222" stroke-width="2"><path d="M2 2l21 21L2 44"/></svg>
<div class="abs avatar" role="img" aria-label="Portrait photo of the team manager"></div>
<div class="abs role">MANAGER</div>
<div class="abs person">Elena Marsh</div>
<div class="abs btn-outline">READ MORE</div>
<div class="abs dots"><span></span><span class="on"></span></div>

<section class="abs blog"></section>
<h2 class="abs blog-title">BLOG</h2>
<div class="abs post-img" style="left:117px" role="img" aria-label="Black and white photo of colleagues in a business discussion"></div>
<div class="abs post-card" style="left:146px">
  <div class="post-title">Post 1 Headline</div>
  <p class="post-body">Sample small text. Lorem ipsum dolor sit amet.</p>
  <span class="post-link">Read More</span>
</div>
<div class="abs post-img" style="left:617px" role="img" aria-label="Black and white photo of a smiling business team"></div>
<div class="abs post-card" style="left:646px">
  <div class="post-title">Post 1 Headline</div>
  <p class="post-body">Sample small text. Lorem ipsum dolor sit amet.</p>
  <span class="post-link">Read More</span>
</div>

<h2 class="abs contact-title">Just Reach Us<br>Right Here</h2>
<label class="abs field-label" style="top:3483px">Name</label>
<div class="abs field" style="top:3503px;height:40px"></div>
<label class="abs field-label" style="top:3564px">Email</label>
<div class="abs field" style="top:3584px;height:40px">Enter a valid email address</div>
<label class="abs field-label" style="top:3645px">Message</label>
<div class="abs field" style="top:3665px;height:106px">Enter your message</div>
<div class="abs submit">Submit</div>

<div class="abs social-head">Let's Get Social!</div>
<div class="abs social" style="top:3402px"><div class="social-box"></div><div class="social-name">Newsroom</div><div class="social-handle">@sampletext</div></div>
<div class="abs social" style="top:3546px"><div class="social-box"></div><div class="social-name">Gallery</div><div class="social-handle">@sampletext</div></div>
<div class="abs social" style="top:3690px"><div class="social-box"></div><div class="social-name">Updates</div><div class="social-handle">@sampletext</div></div>

<footer class="abs site-footer"></footer>
<nav class="abs footer-nav"><span class="active">Home</span><span>About Company</span><span>The Team</span><span>What We Do</span><span>Blog</span><span>Contact Us</span></nav>
<p class="abs copyright">© 2020 <b>NORTHWELL STRATEGY.</b> All Rights Reserved.</p>

</body>
</html>
```